Truck wrap for business Classic design but eye catching

Im looking to wrap several vehicles for my business. I dont really want the expense of a full wrap a partial wrap is fine. I want the wrap to look classy and not busy or gimmicky. Our business is building custom cabinets so I have included a few pictures of jobs that could possibly be backgrounds.
We dont have a specific color for the business logo. The vehicles we have are all white to start with. Our phone number is 512-374-8826

```html
<!DOCTYPE html>
<html lang="en">
<head>
<meta charset="UTF-8">
<title>Ridgeline Woodworks – Vehicle Wrap Side Panel</title>
<link href="https://fonts.googleapis.com/css2?family=Oswald:wght@600&family=Montserrat:wght@500;600&display=swap" rel="stylesheet">
<style>
  :root {
    --page: #f4f4f2;
    --wrap-white: #ffffff;
    --olive: #34352a;
    --olive-soft: #4a4b3b;
    --wood: #9a7a5c;
    --ink: #34352a;
  }
  html, body {
    margin: 0;
    width: 1200px;
    height: 1200px;
    overflow: hidden;
    background: var(--page);
  }
  .wrap-panel {
    position: absolute;
    left: 50px;
    top: 390px;
    width: 1100px;
    height: 420px;
  }
  .wrap-art {
    position: absolute;
    inset: 0;
    width: 1100px;
    height: 420px;
  }
  .brand {
    position: absolute;
    left: 110px;
    top: 58px;
    width: 600px;
    text-align: center;
    color: var(--ink);
  }
  .brand-name {
    font-family: "Oswald", sans-serif;
    font-weight: 600;
    font-size: 56px;
    line-height: 1;
    letter-spacing: 1px;
    text-transform: uppercase;
    white-space: nowrap;
    padding-bottom: 10px;
    border-bottom: 4px solid var(--ink);
  }
  .brand-tagline {
    font-family: "Montserrat", sans-serif;
    font-weight: 500;
    font-size: 22px;
    line-height: 1.2;
    letter-spacing: 9px;
    text-transform: uppercase;
    white-space: nowrap;
    margin-top: 12px;
  }
  .phone {
    display: flex;
    align-items: center;
    gap: 14px;
    margin-top: 14px;
    font-family: "Montserrat", sans-serif;
    font-weight: 600;
    font-size: 40px;
    line-height: 1.1;
    letter-spacing: 3px;
    white-space: nowrap;
  }
  .phone-rule {
    flex: 1;
    height: 3px;
    background: var(--ink);
  }
</style>
</head>
<body>
  <div class="wrap-panel">
    <svg class="wrap-art" viewBox="0 0 1100 420" xmlns="http://www.w3.org/2000/svg">
      <defs>
        <linearGradient id="kitchenTone" x1="0" y1="0" x2="0" y2="1">
          <stop offset="0" stop-color="#e4e6e7"/>
          <stop offset="0.55" stop-color="#f3f4f4"/>
          <stop offset="0.8" stop-color="#cfd1d1"/>
          <stop offset="1" stop-color="#a88a6c"/>
        </linearGradient>
        <linearGradient id="bandTone" x1="0" y1="0" x2="1" y2="0">
          <stop offset="0" stop-color="#34352a"/>
          <stop offset="0.55" stop-color="#3d3d30"/>
          <stop offset="0.75" stop-color="#8a6d52"/>
          <stop offset="1" stop-color="#9a7a5c"/>
        </linearGradient>
        <radialGradient id="jobTone" cx="0.5" cy="0.5" r="0.6">
          <stop offset="0" stop-color="#c08a55"/>
          <stop offset="1" stop-color="#6b4a2e"/>
        </radialGradient>
      </defs>

      <rect class="kitchen-photo" role="img" aria-label="Photo of a bright white custom kitchen with pendant lights and wood floor" x="640" y="0" width="460" height="340" rx="24" fill="url(#kitchenTone)"/>

      <rect class="base-band" x="0" y="300" width="1100" height="120" fill="url(#bandTone)"/>

      <path class="logo-field" d="M0,0 H740 Q880,0 880,140 Q880,300 700,305 H0 Z" fill="var(--wrap-white)"/>
      <path class="logo-field-edge" d="M740,0 Q880,0 880,140 Q880,300 700,305 H0" fill="none" stroke="var(--olive)" stroke-width="16"/>

      <g class="job-thumbnails">
        <circle role="img" aria-label="Photo of a finished cabinetry job" cx="225" cy="305" r="33" fill="url(#jobTone)" stroke="#ffffff" stroke-width="5"/>
        <circle role="img" aria-label="Photo of a finished kitchen installation" cx="305" cy="305" r="33" fill="url(#jobTone)" stroke="#ffffff" stroke-width="5"/>
      </g>
    </svg>

    <div class="brand">
      <div class="brand-name">Ridgeline Woodworks</div>
      <div class="brand-tagline">Custom Cabinetry</div>
      <div class="phone">
        <span class="phone-rule"></span>
        <span class="phone-number">512-374-8826</span>
        <span class="phone-rule"></span>
      </div>
    </div>
  </div>
</body>
</html>
```